Info graphic

I want to design a visual info graphic I can take with me to present my company to membership organisations. The purpose of which is to ask them to allow us to contact their members.
The business is called quillmarsh (www.quillmarshpro.example)
We are a software developer that has created an app for marketing people to search from a list of UK journalists and distribute press releases.
Quillmarsh for Member Organisations
- Want to add value to your members by enhancing your membership package?
- Looking for ways to increase member retention rates?
- Does your organisation exist to champion and raise the profile of your sector?
- Would your members benefit from being empowered to better raise their profile in relevant media?
If the answer is yes to any or all of these questions, Quillmarsh's offering for Member Organisations was created with your needs in mind.
Who are Quillmarsh and why can we benefit organisations like you?
Quillmarsh is a unique PR software company which makes world class PR a reality for any company 'doing PR' in house.
We partner with organisations, so that you are able to add tangible PR value to your members and raise your organisations profile more effectively too.
How does Quillmarsh for Member Organisations work?
(1) We show you Quillmarsh works and how it will benefit your members
(2) We provide your organisation with a complimentary version of Quillmarsh for your own PR use in exchange for an endorsement of the product from you
(3) Your members can be given a preferential rate to Quillmarsh as part of your member package
(4) Your organisation can earn a financial kickback for every member who signs up to Quillmarsh
Member Organisation Case Study
CASE STUDY
Name: Gerald Whitcombe
Position: Director
Organisation: Forged by the Fenwick
Sector: Industrial
Number of member companies: 250+
"Traditionally, many of our manufacturing member firms would not be 'doing PR' and not enjoying the benefits of targeted positive exposure in national industry press or local business press. Working with Quillmarsh has allowed us to make this accessible to our members, ensuring that they understand Forged by the Fenwick were the conduit or 'introducing factor' to Quillmarsh as part of their membership package.
I believe this has enriched our membership package and definitely helped us retain clients and add value to them. The result has been an increase in membership levels and also a dramatic increase in the amount of positive media coverage for many of our members. This also reflects positively on our sector as a whole and in particular the Midlands industrialists which we aim to champion as an organisation. Furthermore, Quillmarsh has enabled us to further enhance the profile of our own organisation, securing coverage on NTR television and in The Ledgerhall magazine".
Gerald Whitcombe, Director, Forged by the Fenwick
The above is just an overview to help you create the design, please feel free to add, subtract content or change the wording as needed.

```html
<!DOCTYPE html>
<html lang="en">
<head>
<meta charset="utf-8">
<title>Quillmarsh – The New Voice of PR</title>
<link rel="stylesheet" href="https://fonts.googleapis.com/css2?family=Questrial&display=swap">
<style>
  :root {
    --leaf-green: #8cc443;
    --chart-lime: #d4df22;
    --ink: #1a1a1a;
    --paper: #ffffff;
    --font-main: "Questrial", sans-serif;
  }
  * { margin: 0; padding: 0; box-sizing: border-box; }
  html, body {
    width: 1200px;
    height: 1095px;
    overflow: hidden;
    background: var(--paper);
  }
  .canvas {
    position: relative;
    width: 1200px;
    height: 1095px;
    font-family: var(--font-main);
    color: var(--ink);
  }

  /* Brand panel */
  .brand-panel {
    position: absolute;
    left: 22px;
    top: 44px;
    width: 632px;
    height: 387px;
    background: var(--leaf-green);
    border-radius: 200px 0 200px 200px;
  }
  .brand-name {
    position: absolute;
    left: 128px;
    top: 206px;
    font-size: 40px;
    font-weight: 400;
    letter-spacing: 0.5px;
    color: var(--paper);
    line-height: 1;
  }
  .brand-tagline {
    position: absolute;
    left: 128px;
    top: 258px;
    font-size: 13px;
    font-weight: 400;
    letter-spacing: 0.2px;
    color: var(--ink);
  }

  /* Member organisation pitch */
  .member-pitch {
    position: absolute;
    left: 736px;
    top: 42px;
    width: 420px;
    font-size: 23px;
    line-height: 36px;
    color: var(--ink);
  }

  /* Headline */
  .voice-headline {
    position: absolute;
    left: 362px;
    top: 622px;
    font-size: 22px;
    font-weight: 400;
    letter-spacing: 0.2px;
    color: var(--ink);
  }

  /* Comparison panel */
  .comparison-panel {
    position: absolute;
    left: 358px;
    top: 665px;
    width: 634px;
    height: 385px;
    background: var(--leaf-green);
    border-radius: 0 180px 200px 200px;
  }

  /* Callout bubble */
  .callout-bubble {
    position: absolute;
    left: 938px;
    top: 401px;
    width: 227px;
    height: 128px;
    background: var(--leaf-green);
    border-radius: 64px 64px 64px 10px;
    display: flex;
    align-items: center;
    justify-content: center;
    text-align: center;
    color: var(--paper);
    font-size: 28px;
    line-height: 41px;
    letter-spacing: 0.5px;
  }

  .chart-layer {
    position: absolute;
    left: 0;
    top: 0;
    width: 1200px;
    height: 1095px;
  }
</style>
</head>
<body>
<main class="canvas">

  <section class="brand-panel" aria-label="Quillmarsh brand">
    <h1 class="brand-name">QUILLMARSH</h1>
    <p class="brand-tagline">MEDIA COVERAGE MADE EASY</p>
  </section>

  <p class="member-pitch">
    Want to add value to your<br>
    members and lift retention?<br>
    Quillmarsh for Member<br>
    Organisations gives your<br>
    members a voice in the media,<br>
    gives you free PR software,<br>
    and earns your organisation<br>
    a kickback for every sign-up.
  </p>

  <h2 class="voice-headline">THE NEW VOICE OF PR</h2>

  <div class="comparison-panel"></div>

  <svg class="chart-layer" viewBox="0 0 1200 1095" role="img" aria-label="Radar chart comparing Quillmarsh with traditional PR methods across reach, targeting, cost, speed, coverage and ease of use">
    <path d="M948 520 C 880 550, 840 600, 828 666" fill="none" stroke="var(--leaf-green)" stroke-width="9" stroke-linecap="round"/>

    <g class="radar" transform="translate(790 856)">
      <circle r="169" fill="var(--chart-lime)" stroke="var(--ink)" stroke-width="1"/>
      <g class="radar-axes" stroke="var(--ink)" stroke-width="0.8">
        <line x1="0" y1="-169" x2="0" y2="169"/>
        <line x1="-146" y1="-84.5" x2="146" y2="84.5"/>
        <line x1="-146" y1="84.5" x2="146" y2="-84.5"/>
      </g>
      <g class="radar-ticks" stroke="var(--ink)" stroke-width="8" stroke-dasharray="1 17" fill="none">
        <line x1="0" y1="0" x2="0" y2="-169"/>
        <line x1="0" y1="0" x2="0" y2="169"/>
        <line x1="0" y1="0" x2="146" y2="-84.5"/>
        <line x1="0" y1="0" x2="146" y2="84.5"/>
        <line x1="0" y1="0" x2="-146" y2="-84.5"/>
        <line x1="0" y1="0" x2="-146" y2="84.5"/>
      </g>
      <polygon class="radar-series"
               points="0,-24 90,-55 90,48 0,142 -93,48 -147,-87"
               fill="none" stroke="var(--ink)" stroke-width="2" stroke-linejoin="round"/>
      <g class="radar-points" fill="var(--paper)" stroke="var(--ink)" stroke-width="1">
        <rect x="-3" y="-27" width="6" height="6"/>
        <rect x="87" y="-58" width="6" height="6"/>
        <rect x="87" y="45" width="6" height="6"/>
        <rect x="-3" y="139" width="6" height="6"/>
        <rect x="-96" y="45" width="6" height="6"/>
        <rect x="-150" y="-90" width="6" height="6"/>
      </g>
    </g>
  </svg>

  <div class="callout-bubble">TRADITIONAL<br>PR METHODS</div>

</main>
</body>
</html>
```